5 Email Newsletter Templates Needed

We need 5 email templates for our email marketing campaign. We are an Insurance Agency in Los Angeles called KPT-Silverbrook Insurance Services. We use Mailvance Hub as our email marketing platform. The templates need to be simple, a nice header, not to busy and you will need to use our color palette. The first email template we need is for our current clients / prospects. The content we will put in this email will be insurance tips and information, short and simple about 2 small paragraphs. The next 3 templates all need to be the same but different colors. One red, one yellow and one green. These will be alerts from kpt-silverbrook. An example a major earthquake hits we will send a red alert. A legislative change on healthcare and we send a yellow alert. We buy another location and we send a green alert. The last email is for our COINs (Centers of Influence, the people who refer business to us). I uploaded an email from one of our business consultants to give an idea of the size and sophistication we are looking for. I also uploaded our corporate brochure and color palette so you can learn more about our firm.

Target Market(s)

Our target markets are commercial business 1mm plus in revenue, 500 employees, high net worth individuals. Our COINs are CPAs, CFOs, Business Managers

Requirements
Nice to have
• HTML Code is desired. You can also provide just an image file for the header and our email marketing program will do the coding for us.
Should not have
• No cartoon looking graphics. Do not use old-style fonts like Times New Roman.

```html
<!DOCTYPE html>
<html lang="en">
<head>
<meta charset="utf-8">
<title>KPT-Silverbrook Insurance Services Newsletter</title>
<link href="https://fonts.googleapis.com/css2?family=Noto+Sans:wght@400;700&display=swap" rel="stylesheet">
<style>
:root{
  --orange:#c65a0a;
  --orange-dark:#a84a06;
  --teal:#0e7868;
  --teal-text:#0b7a62;
  --panel:#cdccc6;
  --taupe:#a1978e;
  --maroon:#7b3a41;
  --arrow:#a31c1c;
  --ink:#2a2a2a;
  --muted:#7d7a76;
  --white:#ffffff;
  --photo-cool:#8a9aaa;
  --photo-warm:#9a6a4a;
}
*{margin:0;padding:0;box-sizing:border-box}
html,body{width:860px;height:1200px;overflow:hidden;background:var(--teal)}
body{position:relative;font-family:"Noto Sans",Tahoma,Verdana,sans-serif;color:var(--ink);font-size:13px}
.abs{position:absolute}
.topbar{left:0;top:0;width:860px;height:47px;background:var(--orange)}
.nav{right:20px;top:0;height:47px;display:flex;gap:58px;align-items:center;list-style:none}
.nav li{color:var(--white);font-size:14px;display:flex;align-items:center;gap:8px;text-transform:uppercase}
.nav li::before{content:"";width:9px;height:9px;border-radius:50%;background:#d9c38a;box-shadow:inset -2px -2px 0 #8c7440}
.frame{left:17px;top:54px;width:826px;height:1093px;background:var(--panel)}
.logo{left:20px;top:57px;width:429px;height:83px;background:var(--white);border:3px solid var(--teal);display:flex;align-items:center;justify-content:center;gap:12px}
.logo-mark{width:22px;height:22px;background:var(--teal)}
.logo-name{font-weight:700;color:var(--teal);font-size:22px;letter-spacing:1px}
.photo{display:block}
.issue{left:469px;top:60px;width:372px;height:241px;border-radius:18px;background:#dedcd6;border:1px solid #b8b6b0;overflow:hidden}
.issue-tab{left:509px;top:57px;width:241px;height:25px;background:linear-gradient(#f4f4f2,#c9c8c3);color:var(--teal-text);font-weight:700;font-size:17px;text-align:center;line-height:25px}
.issue ul{list-style:none;position:absolute;left:22px;top:42px}
.bullet-list li{display:flex;align-items:center;gap:12px;color:var(--teal-text);font-size:13px;line-height:26px;white-space:nowrap}
.bullet-list li::before{content:"";width:12px;height:12px;border-radius:50%;background:#e9dcc0;border:1px solid #b9914e;box-shadow:inset 0 0 0 3px #e9dcc0;background-color:#a7703a;flex:none}
.issue-band{position:absolute;left:0;bottom:0;width:100%;height:54px;background:var(--maroon);color:var(--white);font-weight:700;font-size:15px;text-align:center;line-height:54px}
.section-title{display:flex;align-items:center;gap:8px;color:var(--muted);font-size:15px}
.section-title svg{flex:none}
.rule{border-top:1px solid #a8a59f}
.date-row{left:26px;width:235px;height:26px;border:1px solid #a8a59f;background:#dcdbd6;display:flex;font-size:14px}
.date-row .day{width:90px;padding-left:4px;color:var(--muted);line-height:24px;border-right:1px solid #a8a59f}
.date-row .date{flex:1;padding-left:6px;font-weight:700;color:#6d6a66;line-height:24px}
.teal-text{color:var(--teal-text);font-size:13px;line-height:17px}
.headline-box{left:264px;top:364px;width:580px;height:244px;background:var(--taupe)}
.headline-title{left:284px;top:370px;font-size:17px;color:#1e1e1e}
.body-text{color:#3e3832;font-size:13px;line-height:17px;text-align:justify}
.feature-title{font-weight:700;color:var(--teal-text);font-size:13px}
.more{color:var(--teal-text);font-size:13px}
.invest-box{left:264px;top:922px;width:580px;height:225px;background:var(--taupe)}
.invest-title{left:300px;top:928px;font-size:17px;color:#1e1e1e}
.footer{left:0;top:1154px;width:860px;height:46px;background:var(--orange)}
.copyright{left:26px;top:1167px;color:var(--white);font-weight:700;font-size:14px}
.footer-btn{top:1161px;height:32px;border:1px solid var(--white);border-radius:8px;background:var(--orange-dark);color:#1a1a1a;font-weight:700;font-size:15px;text-align:center;line-height:30px}
</style>
</head>
<body>
<div class="abs topbar"></div>
<ul class="abs nav"><li>About Us</li><li>Advertising</li><li>Contact Us</li></ul>
<div class="abs frame"></div>

<div class="abs logo"><span class="logo-mark"></span><span class="logo-name">KPT-SILVERBROOK INSURANCE SERVICES</span></div>
<div class="abs photo" role="img" aria-label="Group photo of business team" style="left:20px;top:143px;width:429px;height:212px;background:linear-gradient(135deg,#5a4a44,#8a7266 50%,#3a3436)"></div>

<div class="abs issue">
  <ul class="bullet-list">
    <li>Lorem ipsum dolor sit amet, onsectetuer</li>
    <li>adipiscing elit, sed diam nonummy nibh</li>
    <li>euismod tincidunt ut liquam Ut wisi enim ad mi</li>
    <li>nimveniam. Quis nostrud exerci tateuismod tin</li>
    <li>cidunt ut aliquam Ut wisi enim ad minim veni</li>
  </ul>
  <div class="issue-band">Issue No.001, January 25, 2011</div>
</div>
<div class="abs issue-tab">in today's issue</div>

<!-- Left column -->
<div class="abs section-title" style="left:28px;top:381px"><svg width="20" height="10"><path d="M0 5h14M10 1l6 4-6 4" stroke="var(--arrow)" stroke-width="2" fill="none"/></svg>news &amp; events</div>
<div class="abs rule" style="left:26px;top:408px;width:235px"></div>
<div class="abs date-row" style="top:419px"><span class="day">Thursday</span><span class="date">February 3, 2011</span></div>
<p class="abs teal-text" style="left:28px;top:464px;width:220px">Lorem ipsum dolor sit amet, consectetuepiscing elit, sed diam nonummy nibh euismoenim ad minim veniam. Quis nostrud</p>
<div class="abs date-row" style="top:549px"><span class="day">Monday</span><span class="date">February 7, 2011</span></div>
<div class="abs photo" role="img" aria-label="Sell and Buy keyboard keys" style="left:26px;top:582px;width:235px;height:87px;background:linear-gradient(90deg,#9a9a9a,#3a3a3a 50%,#9a9a9a)"></div>
<p class="abs teal-text" style="left:28px;top:676px;width:220px">Lorem ipsum dolor sit amet, consectetuepiscing elit, sed diam nonummy nibh euismoenim ad minim veniam. Quis nostrud</p>
<div class="abs rule" style="left:26px;top:757px;width:235px"></div>
<div class="abs section-title" style="left:28px;top:761px"><svg width="20" height="10"><path d="M0 5h14M10 1l6 4-6 4" stroke="var(--arrow)" stroke-width="2" fill="none"/></svg>overview</div>
<ul class="abs bullet-list" style="left:34px;top:794px;list-style:none">
  <li>Lorem ipsum dolor sit amet,</li>
  <li>adipiscing elit, sed diam nonu</li>
  <li>euismod tincidunt ut liquam</li>
  <li>nimveniam. Quis nostrud ex</li>
</ul>
<div class="abs rule" style="left:26px;top:926px;width:235px"></div>
<div class="abs section-title" style="left:28px;top:937px"><svg width="20" height="10"><path d="M0 5h14M10 1l6 4-6 4" stroke="var(--arrow)" stroke-width="2" fill="none"/></svg>in the spotlight</div>
<div class="abs photo" role="img" aria-label="Discount keyboard key close-up" style="left:28px;top:966px;width:230px;height:86px;background:linear-gradient(90deg,#d8d8d8,#8e8e8e);border:1px solid #eee"></div>
<div class="abs photo" role="img" aria-label="Invest keyboard key close-up" style="left:28px;top:1059px;width:230px;height:88px;background:linear-gradient(135deg,#7a7a7a,#d0d0d0);border:1px solid #eee"></div>

<!-- Right column -->
<div class="abs headline-box"></div>
<div class="abs headline-title">Today's business headline</div>
<div class="abs photo" role="img" aria-label="Sailboat at sea" style="left:277px;top:404px;width:157px;height:189px;background:linear-gradient(160deg,#cfd8e0,#3a5a80 60%,#1e2e44);border:1px solid #eee"></div>
<div class="abs" style="left:451px;top:401px;width:380px">
  <p class="body-text">Lorem ipsum dolor sit amet, consectetuepiscing elit, sed diam nonummy nibh euismod tincidunt ut aliquam erat volutpat. Ut wisi enim ad minim veniam. Quis nostrud exerci tation ullamcorper suscipit lobortis nisl ut aliquip ex ea commodo consequat. Duis autem vel eum iriure dolor in hendrerit in vulputate velit consequat.</p>
  <p class="body-text" style="margin-top:17px">Illum dolore eu feugiat nulla facilisis at vero eros et accumsan et iusto odio dignissim qui blandit. Praesent luptatum zzril delenit augue duis d</p>
</div>

<div class="abs section-title" style="left:270px;top:611px"><svg width="20" height="10"><path d="M0 5h14M10 1l6 4-6 4" stroke="var(--arrow)" stroke-width="2" fill="none"/></svg>latest featured projects</div>
<div class="abs photo" role="img" aria-label="Industrial machinery parts" style="left:265px;top:639px;width:92px;height:132px;background:linear-gradient(135deg,#b04040,#d8d8d8 60%,#666)"></div>
<div class="abs photo" role="img" aria-label="Production line conveyor" style="left:376px;top:639px;width:93px;height:132px;background:linear-gradient(135deg,#6a6a3a,#c0b060 50%,#444)"></div>
<div class="abs photo" role="img" aria-label="Silver car detail" style="left:265px;top:783px;width:92px;height:127px;background:linear-gradient(135deg,#555,#ddd 55%,#777)"></div>
<div class="abs photo" role="img" aria-label="Medical scanner" style="left:376px;top:783px;width:93px;height:127px;background:radial-gradient(circle at 50% 55%,#7a8aa0,#e8e6e0 60%)"></div>

<div class="abs" style="left:484px;top:637px;width:330px">
  <p class="feature-title">Lorem ipsum dolor sit amet,</p>
  <p class="teal-text" style="margin-top:10px">consectetuepiscing elit, sed diam nonummy nibh euismoenim ad minim veniam. Quis nostrud</p>
  <p class="more" style="margin-top:8px">&gt;&gt; more info</p>
  <p class="feature-title" style="margin-top:6px">Lorem ipsum dolor sit amet,</p>
  <p class="teal-text" style="margin-top:10px">consectetuepiscing elit, sed diam nonummy nibh euismoenim ad minim veniam. Quis nostrud</p>
  <p class="more" style="margin-top:8px">&gt;&gt; more info</p>
  <p class="feature-title" style="margin-top:6px">Lorem ipsum dolor sit amet,</p>
  <p class="teal-text" style="margin-top:10px">consectetuepiscing elit, sed diam nonummy nibh euismoenim ad minim veniam. Quis nostrud</p>
  <p class="more" style="margin-top:8px">&gt;&gt; more info</p>
</div>

<div class="abs invest-box"></div>
<svg class="abs" style="left:277px;top:934px" width="20" height="10"><path d="M0 5h14M10 1l6 4-6 4" stroke="var(--arrow)" stroke-width="2" fill="none"/></svg>
<div class="abs invest-title">Investment news</div>
<div class="abs" style="left:278px;top:960px;width:313px">
  <p class="body-text"><b>Lorem ipsum dolor sit amet, consectetuepiscing elit, sed diam nonummy nibh euismod tincidunt ut aliquam</b> erat volutpat. Ut wisi enim ad minim veniam. Quis nostrud exerci tation ullamcorper suscipit lobortis nisl ut aliquip ex ea commodo consequat. Duis autem vel eum iriure dolor in hendrerit in vulputate velit consequat.</p>
  <p class="body-text" style="margin-top:17px">Illum dolore eu feugiat nulla facilisis at vero eros et accumsan et iusto odio dignissim qui qu</p>
</div>
<div class="abs photo" role="img" aria-label="Elegant home interior with staircase and piano" style="left:667px;top:933px;width:166px;height:204px;background:linear-gradient(160deg,#e8d8b8,#b0704a 55%,#5a2a1a);border:1px solid #eee"></div>

<!-- Footer -->
<div class="abs footer"></div>
<div class="abs copyright">© Company Name. All Rights Reserved</div>
<div class="abs footer-btn" style="left:387px;width:122px">Subsribe</div>
<div class="abs footer-btn" style="left:523px;width:125px">Unsubsribe</div>
<div class="abs footer-btn" style="left:658px;width:173px">Change of Email</div>
</body>
</html>
```